Flyerdesign DIN A4 Lang 6-seitig Wickelfalz für Seniorenhilfsverband
Flott - engagiert und entgegenkommend. Gerne wieder!
Zielgruppe
Die Dachorganisation betreibt mehrere Pflegeheime mit unterschiedlichen Themen (Demenz, körperliche Behinderung, etc...) sowie betreutes wohnen und ein Tageszentrum. Auch Verantaltungen und Seminare werden geboten.
Aufgabenstellung
GESUCHT ist ein FLYER-Design.
DIN A4 Lang 6-seitig Wickelfalz.
Es gibt bereits ein fertiges Webdesign, auf dessen Basis ein passendes Design für einen Wickelfalz-Flyer erstellt werden soll. Die Inhaltsdaten sowie ein BSP-Flyer sind im Download-ZIP. Was nun gebraucht wird ist ein ansprechendes Design ohne Inhalt für diesen Verband.

```html
<!DOCTYPE html>
<html lang="de">
<head>
<meta charset="utf-8">
<title>Wickelfalz-Flyer – Außen- und Innenseite</title>
<link rel="stylesheet" href="https://fonts.googleapis.com/css2?family=Montserrat:wght@500&display=swap">
<style>
  :root {
    --page: #ffffff;
    --yellow-soft: #fde48f;
    --yellow-band: #fde7a0;
    --yellow-bright: #fcd966;
    --yellow-inner: #fde391;
    --olive: #b2a67e;
    --slate: #616161;
    --fold: #c9c2a8;
    --fold-inner: #8f866a;
    --brand: #b59a3a;
    --frame: #c8c8d0;
  }
  * { margin: 0; padding: 0; box-sizing: border-box; }
  html, body { width: 982px; height: 1200px; overflow: hidden; background: var(--page); }
  .canvas { position: relative; width: 982px; height: 1200px; }

  .sheet { position: absolute; left: 82px; width: 818px; height: 576px; overflow: hidden; }
  .sheet--outside {
    top: 22px;
    border: 1px solid var(--frame);
    background: linear-gradient(90deg, var(--yellow-soft) 0%, var(--yellow-soft) 55%, #fffdf7 100%);
  }
  .sheet--inside { top: 604px; background: var(--yellow-inner); }

  .outside__spine { position: absolute; left: 0; top: 0; width: 9px; height: 100%; background: var(--slate); }
  .outside__header {
    position: absolute; left: 9px; top: 0; right: 0; height: 113px;
    background: linear-gradient(90deg, var(--yellow-band) 0%, #fde68f 50%, #fff6d8 100%);
    border-bottom: 4px solid var(--slate);
  }
  .outside__corner { position: absolute; right: 0; top: 0; width: 62px; height: 113px; background: var(--slate); }
  .fold { position: absolute; top: 0; width: 2px; height: 100%; background: var(--fold); }
  .fold--inner { background: var(--fold-inner); }

  .emblem-area {
    position: absolute; left: 322px; top: 140px; width: 330px; height: 330px;
    background: radial-gradient(circle, rgba(178,160,80,0.55) 0%, rgba(178,160,80,0.25) 45%, rgba(178,160,80,0) 70%);
  }

  .brand {
    position: absolute; display: flex; flex-direction: column; align-items: center; gap: 4px;
    font-family: "Montserrat", sans-serif; font-weight: 500; font-size: 9px;
    letter-spacing: 0.08em; color: var(--brand);
  }
  .brand__dot { width: 22px; height: 22px; border-radius: 50%; background: var(--brand); opacity: 0.8; }
  .brand--outside { right: 14px; bottom: 8px; }
  .brand--inside { left: 392px; bottom: 10px; }

  .inside__shapes { position: absolute; inset: 0; }
</style>
</head>
<body>
<main class="canvas">

  <section class="sheet sheet--outside" aria-label="Außenseite">
    <div class="outside__spine"></div>
    <div class="outside__header"></div>
    <div class="outside__corner"></div>
    <div class="fold" style="left:270px"></div>
    <div class="fold" style="left:545px"></div>
    <div class="emblem-area" role="img" aria-label="Große dezente Sonnen-Grafik als Titelmotiv"></div>
    <div class="brand brand--outside">
      <span class="brand__dot"></span>
      <span class="brand__name">LICHTHOF</span>
    </div>
  </section>

  <section class="sheet sheet--inside" aria-label="Innenseite">
    <svg class="inside__shapes" width="818" height="576" viewBox="0 0 818 576">
      <ellipse cx="0" cy="288" rx="265" ry="300" fill="var(--yellow-bright)"/>
      <ellipse cx="800" cy="288" rx="535" ry="292" fill="var(--olive)"/>
    </svg>
    <div class="fold fold--inner" style="left:265px"></div>
    <div class="fold fold--inner" style="left:539px"></div>
    <div class="brand brand--inside">
      <span class="brand__dot"></span>
      <span class="brand__name">LICHTHOF</span>
    </div>
  </section>

</main>
</body>
</html>
```